Property Investment eBook Cover

I am a long established Australian property investment adviser, analyst and consultant who is now in semi-retired mode and have re-branded to reflect a more casual and personal approach to advising my property investor clients. I am writing a 'revised edition' to a book written in partnership with my father 20 years ago and need an eBook Cover for this new edition. The eBook will be uploaded to all the regular Australian providers (Larkfield Reader, Quince Folio, Tavi, Pagemarten)

The 3 key elements in the book cover are:

Title: The Harvest Engine of Land. The word 'Property' should be larger and more prominent. eg "The Wealth Power of" could be 1/3 the size of "Property" - with both justified left

Edition: Sydney 2021. "Sydney 2021" should be the focus and dominant imagery of the eBook cover and more prominent than the Title or Author

Author: Colin Marsh, The Housing Ledger Guide. The word "Author" should not appear. "The Housing Ledger Guide" should appear underneath Colin Marsh and justified to Colin Marsh, therefore a smaller font.

The cover should be simple, but eye-catching. No property images, more of an abstract background, than a background with an image. Our preferred colour palette is more blues/greens. Prefer SerifFonts

Copy of book published 20 years ago attached for reference only

```html
<!DOCTYPE html>
<html lang="en">
<head>
<meta charset="utf-8">
<title>The Harvest Engine of Land — Sydney 2021</title>
<link rel="stylesheet" href="https://fonts.googleapis.com/css2?family=Playfair+Display+SC:wght@400;700&family=Cormorant+Garamond:wght@500&display=swap">
<style>
  :root {
    --aqua-light: #c4e4e6;
    --aqua: #a6d5da;
    --aqua-deep: #7fc1c9;
    --band: #ffffff;
    --rule: #3d4a4c;
    --ink: #0c0c0c;
    --shadow: rgba(20, 40, 45, 0.42);
  }
  html, body {
    margin: 0;
    padding: 0;
    width: 750px;
    height: 1200px;
    overflow: hidden;
    background: var(--band);
  }
  .cover {
    position: relative;
    width: 750px;
    height: 1200px;
    overflow: hidden;
  }
  .backdrop {
    position: absolute;
    left: 0;
    width: 750px;
  }
  .backdrop--top {
    top: 0;
    height: 628px;
    background: linear-gradient(155deg, var(--aqua-light) 0%, var(--aqua) 38%, var(--aqua-deep) 62%, var(--aqua) 85%, var(--aqua-light) 100%);
  }
  .backdrop--bottom {
    top: 783px;
    height: 417px;
    background: linear-gradient(200deg, var(--aqua-deep) 0%, var(--aqua) 40%, var(--aqua-light) 70%, var(--aqua) 100%);
  }
  .edition-band {
    position: absolute;
    top: 628px;
    left: 0;
    width: 750px;
    height: 155px;
    background: var(--band);
    border-top: 1px solid var(--rule);
    border-bottom: 1px solid var(--rule);
    box-sizing: border-box;
  }
  .type-layer {
    position: absolute;
    inset: 0;
    width: 750px;
    height: 1200px;
    fill: var(--ink);
    font-family: "Playfair Display SC", "Bodoni Moda", serif;
    font-weight: 400;
  }
  .title-word {
    filter: drop-shadow(7px 9px 6px var(--shadow));
  }
  .title-article { font-size: 58px; }
  .title-harvest { font-size: 164px; }
  .title-engine  { font-size: 106px; }
  .title-of      { font-size: 46px; }
  .title-land    { font-size: 110px; }
  .edition       { font-size: 94px; font-weight: 700; }
  .author-name   { font-size: 96px; }
  .author-role {
    font-family: "Cormorant Garamond", "Goudy Bookletter 1911", serif;
    font-weight: 500;
    font-size: 44px;
  }
</style>
</head>
<body>
  <main class="cover">
    <div class="backdrop backdrop--top" role="img" aria-label="Abstract aqua alcohol-ink marble with teal veins and flecks of rose gold"></div>
    <div class="edition-band"></div>
    <div class="backdrop backdrop--bottom" role="img" aria-label="Abstract aqua alcohol-ink marble with teal veins and flecks of rose gold"></div>

    <svg class="type-layer" viewBox="0 0 750 1200" aria-label="The Harvest Engine of Land, Sydney 2021, Colin Marsh, The Housing Ledger Guide">
      <g class="title">
        <text class="title-word title-article" x="353" y="150" textLength="83" lengthAdjust="spacingAndGlyphs">The</text>
        <text class="title-word title-harvest" x="122" y="253" textLength="531" lengthAdjust="spacingAndGlyphs">Harvest</text>
        <text class="title-word title-engine" x="166" y="375" textLength="378" lengthAdjust="spacingAndGlyphs">Engine</text>
        <text class="title-word title-of" x="566" y="375" textLength="50" lengthAdjust="spacingAndGlyphs">of</text>
        <text class="title-word title-land" x="116" y="506" textLength="537" lengthAdjust="spacing">Land</text>
      </g>

      <text class="edition" x="162" y="731" textLength="476" lengthAdjust="spacingAndGlyphs">Sydney 2021</text>

      <g class="author">
        <text class="author-name" x="90" y="1084" textLength="566" lengthAdjust="spacingAndGlyphs">Colin Marsh</text>
        <text class="author-role" x="153" y="1134" textLength="447" lengthAdjust="spacingAndGlyphs">The Housing Ledger Guide.</text>
      </g>
    </svg>
  </main>
</body>
</html>
```